Varga Lillas Physiotherapy Business Card Vienna

We need a business card design for a newly created Physiotherapy company based in Vienna Austria.
We seek a simple, modern, minimalist design without too much color variation. The font should look young/fresh, but definitely not childish or so. Since we are a starting Business, we currently haven't got a logo, if you feel like a logo would fit your design, feel free to use one, but it's not necessary.
Target Market(s)
Healthcare, young and elderly people with mobility issues
Industry/Entity Type
Health And Wellness
Contact Information for Business Card
Name: Lilla Varga
Title description: Physiotherapist
Phone num: +43 664 5290 4816
e-mail: lilla.praxis@brelomail.com
Colors
Designer to choose colors to be used in the design.
Requirements
Must have
- Final design language must be in German, basically, the Title Description needs to be "Physiotherapeutin" the other details remain as in the English Language.
Nice to have
- Simple, modern, minimalist design
Should not have
- too many colors, Obvious use of a skeleton, skull, spline

```html
<!DOCTYPE html>
<html lang="de">
<head>
<meta charset="utf-8">
<title>Lilla Varga – Physiotherapeutin</title>
<link rel="stylesheet" href="https://fonts.googleapis.com/css2?family=Yanone+Kaffeesatz:wght@200&family=Quicksand:wght@300;600&display=swap">
<style>
  :root {
    --backdrop: #2f3e45;
    --card: #141417;
    --accent: #16aee3;
  }
  * { box-sizing: border-box; margin: 0; padding: 0; }
  html, body {
    width: 1200px;
    height: 900px;
    overflow: hidden;
    background: var(--backdrop);
  }
  .business-card {
    position: absolute;
    left: 100px;
    top: 140px;
    width: 1000px;
    height: 620px;
    background: var(--card);
    color: var(--accent);
  }
  .identity {
    position: absolute;
    left: 0;
    right: 0;
    top: 62px;
    text-align: center;
  }
  .identity-name {
    display: block;
    font-family: "Quicksand", sans-serif;
    font-weight: 300;
    font-size: 92px;
    line-height: 1;
    letter-spacing: 1px;
  }
  .identity-title {
    display: block;
    margin-top: 22px;
    font-family: "Quicksand", sans-serif;
    font-weight: 600;
    font-size: 32px;
    letter-spacing: 0.5px;
    line-height: 1;
  }
  .contact {
    position: absolute;
    top: 372px;
    display: flex;
    align-items: center;
    gap: 14px;
    font-family: "Yanone Kaffeesatz", sans-serif;
    font-weight: 200;
    font-size: 42px;
    line-height: 1;
    white-space: nowrap;
  }
  .contact-phone { left: 58px; }
  .contact-mail { left: 508px; }
  .contact-icon {
    width: 62px;
    height: 62px;
    flex: none;
  }
</style>
</head>
<body>
  <article class="business-card">
    <header class="identity">
      <span class="identity-name">Lilla Varga</span>
      <span class="identity-title">Physiotherapeutin</span>
    </header>

    <p class="contact contact-phone">
      <svg class="contact-icon" viewBox="0 0 64 64" aria-hidden="true">
        <circle cx="32" cy="32" r="29" fill="none" stroke="var(--accent)" stroke-width="3"/>
        <path d="M14 27 C14 17 50 17 50 27 L50 30 L42 30 L41 25 C36 23 28 23 23 25 L22 30 L14 30 Z" fill="var(--accent)"/>
        <path d="M25 30 L39 30 L46 44 L18 44 Z" fill="var(--accent)"/>
        <circle cx="32" cy="37" r="3.5" fill="var(--card)"/>
      </svg>
      <span>+43 664 5290 4816</span>
    </p>

    <p class="contact contact-mail">
      <svg class="contact-icon" viewBox="0 0 64 64" aria-hidden="true">
        <circle cx="32" cy="32" r="29" fill="none" stroke="var(--accent)" stroke-width="3"/>
        <text x="32" y="42" text-anchor="middle" font-family="Quicksand, sans-serif" font-weight="600" font-size="30" fill="var(--accent)">@</text>
      </svg>
      <span>lilla.praxis@brelomail.com</span>
    </p>
  </article>
</body>
</html>
```